Engineering Consultant Business Card

I'm starting a new business as a high-end engineering consultant in a niche field. I've attached the jpg for my logo plus the branding guideline document that I've been following. You can see my business website here: www.tarvikworks.com
I'd like a business card that has the logo on one side, then the other side has (in any order): Tarvik Works, Inc.
Dana Whitlock
President and Chief EMC Engineer
www.tarvikworks.com
dana@tarvikworks.com
Optional: motto "We will solve your EMC problems as early as possible—ideally before they even start."
I'm not planning on including a phone number
Target Market(s)
Businesses, especially makers of electronics hardware
Industry/Entity Type
Electrical engineering
Contact Information for Business Card
Company name, my name, website, email

```html
<!DOCTYPE html>
<html lang="en">
<head>
<meta charset="utf-8">
<title>Tarvik Works, Inc. — Business Card</title>
<link rel="stylesheet" href="https://fonts.googleapis.com/css2?family=Montserrat:wght@400;500;700;800&display=swap">
<style>
  :root {
    --brand-blue: #324a9b;
    --ink: #2b2b2b;
    --paper: #ffffff;
    --backdrop: #e6e7ea;
  }
  * { margin: 0; padding: 0; box-sizing: border-box; }
  html, body {
    width: 1200px;
    height: 960px;
    overflow: hidden;
    background: var(--backdrop);
    font-family: "Montserrat", sans-serif;
  }
  .canvas {
    width: 1200px;
    height: 960px;
    display: flex;
    flex-direction: column;
    align-items: center;
    justify-content: center;
    gap: 40px;
  }
  .card {
    position: relative;
    width: 760px;
    height: 434px;
    box-shadow: 0 6px 18px rgba(0, 0, 0, 0.18);
    overflow: hidden;
  }

  /* Front side */
  .card--front {
    background: var(--brand-blue);
    display: flex;
    align-items: center;
    justify-content: center;
  }
  .wordmark {
    display: flex;
    align-items: center;
    gap: 18px;
    font-weight: 800;
    letter-spacing: 0.01em;
  }
  .wordmark__dot {
    border-radius: 50%;
    flex: none;
  }
  .card--front .wordmark { color: var(--paper); font-size: 46px; }
  .card--front .wordmark__dot { width: 40px; height: 40px; border: 7px solid var(--paper); }

  /* Back side */
  .card--back { background: var(--paper); }
  .card--back .wordmark {
    position: absolute;
    top: 58px;
    right: 56px;
    color: var(--brand-blue);
    font-size: 28px;
    gap: 12px;
  }
  .card--back .wordmark__dot { width: 26px; height: 26px; border: 5px solid var(--brand-blue); }

  .contact {
    position: absolute;
    right: 56px;
    top: 190px;
    list-style: none;
    text-align: right;
    font-size: 15px;
    font-weight: 400;
    color: var(--ink);
    letter-spacing: 0.02em;
  }
  .contact__item {
    display: flex;
    align-items: center;
    justify-content: flex-end;
    gap: 10px;
    margin-bottom: 12px;
  }
  .contact__icon { width: 15px; height: 15px; flex: none; }

  .identity {
    position: absolute;
    left: 56px;
    bottom: 54px;
  }
  .identity__name {
    font-size: 36px;
    font-weight: 800;
    color: var(--brand-blue);
    line-height: 1.1;
  }
  .identity__title {
    margin-top: 6px;
    font-size: 17px;
    font-weight: 400;
    color: var(--ink);
    letter-spacing: 0.02em;
  }
</style>
</head>
<body>
  <main class="canvas">
    <section class="card card--front" aria-label="Business card front">
      <div class="wordmark">
        <span class="wordmark__dot" aria-hidden="true"></span>
        <span class="wordmark__name">Tarvik Works</span>
      </div>
    </section>

    <section class="card card--back" aria-label="Business card back">
      <div class="wordmark">
        <span class="wordmark__dot" aria-hidden="true"></span>
        <span class="wordmark__name">Tarvik Works</span>
      </div>

      <ul class="contact">
        <li class="contact__item">
          <span>dana@tarvikworks.com</span>
          <svg class="contact__icon" viewBox="0 0 16 16" aria-hidden="true">
            <rect x="1" y="3" width="14" height="10" rx="1" fill="var(--brand-blue)"/>
            <path d="M1.5 3.8 L8 9 L14.5 3.8" fill="none" stroke="#fff" stroke-width="1.4"/>
          </svg>
        </li>
        <li class="contact__item">
          <span>www.tarvikworks.com</span>
          <svg class="contact__icon" viewBox="0 0 16 16" aria-hidden="true">
            <circle cx="8" cy="8" r="7" fill="var(--brand-blue)"/>
            <g fill="none" stroke="#fff" stroke-width="1">
              <ellipse cx="8" cy="8" rx="3" ry="7"/>
              <line x1="1" y1="8" x2="15" y2="8"/>
              <line x1="2" y1="4.5" x2="14" y2="4.5"/>
              <line x1="2" y1="11.5" x2="14" y2="11.5"/>
            </g>
          </svg>
        </li>
      </ul>

      <div class="identity">
        <h1 class="identity__name">Dana Whitlock</h1>
        <p class="identity__title">President &amp; Chief EMC Engineer</p>
      </div>
    </section>
  </main>
</body>
</html>
```